Design a Logo and Business Card

Please see the requirements here:
https://www.filquarry.com/s/k7trw2mzpvyaelq4x/Requirements.pdf?dl=0
Leave a comment if you have any questions.

```html
<!DOCTYPE html>
<html lang="en">
<head>
<meta charset="utf-8">
<title>Kestrel Painting – Business Card</title>
<link href="https://fonts.googleapis.com/css2?family=Open+Sans:wght@400;600&display=swap" rel="stylesheet">
<style>
  :root {
    --page-bg: #ece9e4;
    --card-bg: #ffffff;
    --brand-red: #e0262f;
    --brand-grey: #5c5c5c;
    --ink: #222222;
    --card-shadow: rgba(60, 40, 20, 0.22);
  }
  * { box-sizing: border-box; margin: 0; padding: 0; }
  html, body {
    width: 1200px;
    height: 912px;
    overflow: hidden;
    background: var(--page-bg);
    font-family: "Open Sans", Arial, sans-serif;
  }
  .stage {
    position: relative;
    width: 1200px;
    height: 912px;
  }
  .card {
    position: absolute;
    width: 525px;
    height: 300px;
    background: var(--card-bg);
    box-shadow: 0 6px 18px var(--card-shadow);
    display: flex;
    flex-direction: column;
    align-items: center;
    justify-content: center;
  }
  .card--front { left: 90px;  top: 120px; }
  .card--back  { left: 585px; top: 490px; }

  .brand {
    display: flex;
    align-items: center;
    gap: 12px;
  }
  .brand__mark {
    width: 22px;
    height: 22px;
    background: var(--brand-red);
  }
  .brand__name {
    font-weight: 400;
    font-size: 30px;
    letter-spacing: 1px;
    text-transform: uppercase;
    color: var(--brand-grey);
  }
  .card--back .brand__mark { width: 30px; height: 30px; }
  .card--back .brand__name { font-size: 40px; }

  .contact {
    margin-top: 22px;
    text-align: center;
  }
  .contact__name {
    color: var(--brand-red);
    font-size: 15px;
    margin-bottom: 12px;
  }
  .contact__line {
    color: var(--ink);
    font-size: 12.5px;
    line-height: 1.5;
  }
</style>
</head>
<body>
  <main class="stage">
    <section class="card card--front" aria-label="Business card front">
      <div class="brand">
        <span class="brand__mark"></span>
        <span class="brand__name">Kestrel Painting</span>
      </div>
      <div class="contact">
        <p class="contact__name">Marta Lindqvist</p>
        <p class="contact__line">+41 98765432</p>
        <p class="contact__line">hello@kestrelpaint.ch</p>
        <p class="contact__line">www.kestrelpaint.ch</p>
      </div>
    </section>

    <section class="card card--back" aria-label="Business card back">
      <div class="brand">
        <span class="brand__mark"></span>
        <span class="brand__name">Kestrel Painting</span>
      </div>
    </section>
  </main>
</body>
</html>
```